Vibrant business card design for Product person in Tech

I'm a 29 y/o female Product manager and I'd like to get a business card designed I can use when networking. I'd love something that stands out. Feel free to experiment with the use of colour, maybe geometrical elements - get creative! I work in the tech industry, so looking for a design without too much of a corporate feel. <br/><br/>The business card should have room for:<br/>Name<br/>Email address<br/>Veltrio

Target Market(s)

Tech

Contact Information for Business Card

Name
Email
Veltrio

Colors
faa54b
00a990
33b8a4
abd037
fbee3f
e667a6
ffcf3e
f59195

```html
<!DOCTYPE html>
<html lang="en">
<head>
<meta charset="utf-8">
<title>Dana Whitfield — Business Card</title>
<link href="https://fonts.googleapis.com/css2?family=Rubik:wght@400;500&display=swap" rel="stylesheet">
<style>
  :root {
    --stage: #a9a9a9;
    --card: #1b1c1e;
    --accent: #33b8a4;
    --accent-warm: #faa54b;
    --text: #eef0f2;
    --muted: #c3c7cc;
    --globe-teal: #00a990;
    --globe-mint: #33b8a4;
    --globe-lime: #abd037;
    --globe-pink: #e667a6;
    --globe-gold: #ffcf3e;
  }
  * { box-sizing: border-box; margin: 0; padding: 0; }
  html, body { width: 1200px; height: 930px; overflow: hidden; }
  body {
    background: var(--stage);
    font-family: "Rubik", Arial, sans-serif;
    position: relative;
  }
  .card {
    position: absolute;
    width: 560px;
    height: 320px;
    border-radius: 22px;
    background: var(--card);
    overflow: hidden;
  }
  .card--front { left: 90px; top: 110px; }
  .card--back { left: 550px; top: 500px; }

  .globe-art { position: absolute; }
  .card--front .globe-art {
    width: 210px; height: 210px;
    left: 175px; top: 55px;
    border-radius: 50%;
    background:
      radial-gradient(circle at 35% 30%, var(--globe-gold) 0%, transparent 30%),
      radial-gradient(circle at 70% 70%, var(--globe-pink) 0%, transparent 45%),
      radial-gradient(circle at 45% 45%, var(--globe-mint) 0%, var(--globe-teal) 55%, #0c5f57 100%);
    box-shadow: 0 0 30px rgba(51, 184, 164, 0.45);
  }
  .card--back .globe-art {
    inset: 0;
    opacity: 0.55;
    background:
      radial-gradient(ellipse 40% 55% at 78% 40%, var(--globe-pink) 0%, transparent 100%),
      radial-gradient(ellipse 35% 45% at 20% 75%, var(--globe-lime) 0%, transparent 100%),
      radial-gradient(ellipse 60% 80% at 50% 50%, var(--globe-teal) 0%, transparent 100%);
  }

  .contact {
    position: absolute;
    left: 205px;
    top: 92px;
    color: var(--text);
  }
  .contact__name {
    font-size: 24px;
    font-weight: 500;
    color: var(--accent-warm);
    letter-spacing: 0.5px;
    text-transform: uppercase;
  }
  .contact__role {
    font-size: 16px;
    color: var(--muted);
    margin-top: 4px;
  }
  .contact__list {
    list-style: none;
    margin-top: 16px;
    margin-left: 28px;
  }
  .contact__item {
    display: flex;
    align-items: center;
    gap: 10px;
    font-size: 17px;
    line-height: 24px;
    color: var(--text);
  }
  .contact__icon { width: 14px; height: 14px; flex: none; }
</style>
</head>
<body>
  <section class="card card--front" aria-label="Card front">
    <div class="globe-art" role="img" aria-label="Illustrated globe with continents and a glowing network of connected points"></div>
  </section>

  <section class="card card--back" aria-label="Card back">
    <div class="globe-art" role="img" aria-label="Large faint globe with continents and network lines filling the card"></div>
    <div class="contact">
      <h1 class="contact__name">Dana Whitfield</h1>
      <p class="contact__role">Director</p>
      <ul class="contact__list">
        <li class="contact__item">
          <svg class="contact__icon" viewBox="0 0 24 24"><path fill="var(--accent)" d="M6.6 10.8a15 15 0 0 0 6.6 6.6l2.2-2.2c.3-.3.7-.4 1-.2 1.1.4 2.3.6 3.6.6.6 0 1 .4 1 1V20c0 .6-.4 1-1 1A17 17 0 0 1 3 4c0-.6.4-1 1-1h3.5c.6 0 1 .4 1 1 0 1.3.2 2.5.6 3.6.1.3 0 .7-.2 1z"/></svg>
          (555) 218-4470
        </li>
        <li class="contact__item">
          <svg class="contact__icon" viewBox="0 0 14 14"><circle cx="7" cy="7" r="6" fill="var(--accent)"/></svg>
          Veltrio
        </li>
        <li class="contact__item">
          <svg class="contact__icon" viewBox="0 0 24 24"><rect x="2.5" y="5" width="19" height="14" rx="1.5" fill="none" stroke="var(--accent)" stroke-width="2"/><path d="M3 6l9 7 9-7" fill="none" stroke="var(--accent)" stroke-width="2"/></svg>
          whitfield@mailnest.com
        </li>
      </ul>
    </div>
  </section>
</body>
</html>
```